VELTIQ Business Presentation Powerpoint

We need a powerpoint template based around our logo/coloursThe powerpoint will be used for 1. business development (sales)2. presentation of reports etc

Looking for snappy ways of presenting data (findings) - graphs, tabulations etc

Target Market(s)

Banks, multinational developers, construction groups
CEO, COO, VP, EGM etc

Industry/Entity Type

Consultant

Colors
3277b5

Requirements
Must have
• Main title page
• Standard Title page
• Tabulations style page
• Listing style page
• Graph style page
• Image with text box (2 on a page) style page
• Essentally all features used in business
Nice to have
• Pie chart style page
• open to amy presentation ideas

```html
<!DOCTYPE html>
<html lang="en">
<head>
<meta charset="utf-8">
<title>VELTIQ Project Oversight – Presentation Template</title>
<link href="https://fonts.googleapis.com/css2?family=Lato:wght@300;400;700;900&display=swap" rel="stylesheet">
<style>
  :root{
    --blue:#3277b5;
    --blue-deep:#2a5f96;
    --blue-soft:#6d9fd0;
    --navy:#2b2f45;
    --ink:#3a3a3a;
    --muted:#8a8f99;
    --rule:#cfd5dd;
    --paper:#ffffff;
    --canvas:#f1f2f4;
    --photo-grey:#9aa3ad;
    --photo-warm:#b9aea2;
  }
  *{box-sizing:border-box;margin:0;padding:0}
  html,body{width:720px;height:1200px;overflow:hidden}
  body{font-family:'Lato',sans-serif;color:var(--ink);background:var(--canvas);position:relative}

  /* ---------- hero ---------- */
  .hero-accent{position:absolute;left:514px;top:0;width:206px;height:395px;background:var(--blue)}
  .features{position:absolute;left:18px;top:44px;width:312px;list-style:none;font-size:16px;line-height:21.3px;color:#474a50;font-weight:700}
  .features li{position:relative;padding-left:25px}
  .features li::before{content:"";position:absolute;left:0;top:3px;width:14px;height:14px;border:2.5px solid #474a50;background:#fff}
  .features li.sub{padding-left:46px;font-weight:400}
  .features li.sub::before{left:34px;top:7px;width:6px;height:6px;border:none;background:#474a50}
  .features li.sub.deep{padding-left:57px}
  .features li.sub.deep::before{left:35px}

  .title-slide{position:absolute;left:330px;top:62px;width:376px;height:211px;background:var(--paper);box-shadow:0 2px 10px rgba(0,0,0,.25);overflow:hidden}
  .title-slide .bar{position:absolute;left:56px;top:87px;width:3px;height:39px;background:var(--blue)}
  .title-slide .wordmark{position:absolute;left:71px;top:80px;font-weight:900;font-size:34px;letter-spacing:1px;color:var(--navy);line-height:1}
  .title-slide .tagline{position:absolute;left:72px;top:116px;font-weight:900;font-size:8.6px;letter-spacing:5.2px;color:var(--navy)}
  .title-slide .chevron-box{position:absolute;left:260px;top:81px;width:116px;height:48px;background:var(--blue);display:flex;align-items:center;padding-left:16px}
  .title-slide .foot{position:absolute;left:33px;top:193px;right:24px;display:flex;align-items:center;gap:6px;font-size:3.6px;font-weight:900;letter-spacing:.6px;color:var(--navy)}
  .title-slide .foot::after{content:"";flex:1;height:.6px;background:var(--rule)}

  /* ---------- slide grid ---------- */
  .slide{position:absolute;width:226px;height:127px;background:var(--paper);overflow:hidden;box-shadow:0 1px 4px rgba(0,0,0,.22)}
  .c1{left:7px}.c2{left:247px}.c3{left:487px}
  .r1{top:399px}.r2{top:535px}.r3{top:671px}.r4{top:802px}.r5{top:933px}.r6{top:1067px}

  .brand{position:absolute;right:9px;top:6px;display:flex;align-items:center;gap:1.5px;font-weight:900;font-size:5px;color:var(--navy);line-height:1}
  .brand .num{width:5px;height:5px;background:var(--blue);color:#fff;font-size:2.6px;display:flex;align-items:center;justify-content:center}
  .footer{position:absolute;left:18px;right:14px;bottom:8px;display:flex;align-items:center;gap:3px;font-size:2px;font-weight:900;letter-spacing:.3px;color:var(--navy)}
  .footer::after{content:"";flex:1;height:.4px;background:var(--rule)}

  .heading{position:absolute;left:18px;top:11px;border-left:1px solid var(--navy);padding-left:3px}
  .kicker{font-size:2.4px;letter-spacing:.2px;color:var(--muted);text-transform:uppercase;line-height:1.2}
  .title{font-size:8.4px;font-weight:700;color:var(--navy);line-height:1.05}
  .title .hl{color:var(--blue)}
  .fine{font-size:2.5px;line-height:1.4;color:#666}
  .fine p+p{margin-top:2.5px}
  .label{font-size:3px;font-weight:700;color:var(--navy);text-transform:uppercase}

  .photo{position:absolute;background:linear-gradient(135deg,var(--photo-grey),#d6dbe0 60%,var(--photo-warm))}
  .photo.cool{background:linear-gradient(160deg,#5c7fa6,#c7d3e0 55%,#8da1b7)}
  .photo.dark{background:linear-gradient(150deg,#2d3136,#5b6068)}
  .photo.site{background:linear-gradient(180deg,#c9ccc5,#8b8470 55%,#4f5860)}
  .photo.blue{background:linear-gradient(135deg,#2f6aa5,#4a87c2 55%,#2c5e92)}
  .caption{position:absolute;left:0;right:0;bottom:0;background:var(--blue);color:#fff;padding:2px 3px}
  .caption b{display:block;font-size:3.4px}
  .caption span{display:block;font-size:2.2px;line-height:1.3;opacity:.9}

  .band{position:absolute;left:0;right:0;top:80px;height:30px;background:rgba(50,119,181,.92);padding:11px 0 0 18px}
  .band .heading-w{border-left:1px solid #fff;padding-left:3px;color:#fff}
  .band .kicker{color:#dbe7f3}
  .band .title{color:#fff}
  .slide-wordmark{position:absolute;left:18px;top:5px;font-weight:900;font-size:11px;color:var(--navy);letter-spacing:.3px}
  .slide-wordmark.light{color:#fff}

  .hero-text{color:#fff;border-left:1px solid #fff;padding-left:4px}
  .hero-text .kicker{color:#dbe7f3}
  .hero-text .big{font-size:10.5px;font-weight:700;line-height:1}
  .hero-text .big.heavy{font-weight:900}
  .hero-text .fine{color:#e6eef7;margin-top:2px}

  .milestone{position:absolute;top:46px;width:56px;height:42px;border:.6px solid var(--blue);text-align:center;padding-top:10px}
  .milestone .icon{position:absolute;left:50%;top:-8px;transform:translateX(-50%);width:13px;height:13px;background:#e9eef4;display:flex;align-items:center;justify-content:center}
  .milestone .year{font-size:6px;color:var(--navy)}
  .milestone .label{text-transform:none;font-size:2.6px;margin:1px 0}
  .milestone .fine{font-size:2px;padding:0 3px}
  .arrow-dot{position:absolute;top:60px;width:11px;height:11px;border-radius:50%;background:var(--blue);display:flex;align-items:center;justify-content:center}

  .member{position:absolute;top:35px;width:39px}
  .member .photo{position:relative;width:39px;height:39px}
  .member .label{font-size:2.8px;margin-top:3px}
  .member .fine{font-size:1.9px}
  .socials{display:flex;gap:1px;margin-top:1.5px}
  .socials i{width:3px;height:3px;background:var(--blue);display:block}

  .chart{position:absolute}
</style>
</head>
<body>

  <!-- hero -->
  <div class="hero-accent"></div>
  <ul class="features">
    <li>Ratio 16:9</li>
    <li>Full HD</li>
    <li>Custom color pallet</li>
    <li>Custom Font -&nbsp; Easy Change</li>
    <li class="sub">Lato Black</li>
    <li class="sub">Lato</li>
    <li>Easy to edit, just drag and drop images</li>
    <li>Can be included up to 100 &nbsp;slides;</li>
    <li class="sub deep">Text + images (1,2,3,4)</li>
    <li class="sub deep">Portfolio Slides</li>
    <li class="sub deep">Text Slides</li>
    <li class="sub deep">Infografics</li>
    <li>In the sample load you will find 19 slides</li>
  </ul>

  <section class="title-slide">
    <div class="bar"></div>
    <div class="wordmark">VELTIQ</div>
    <div class="tagline">PROJECT OVERSIGHT</div>
    <div class="chevron-box">
      <svg width="28" height="22" viewBox="0 0 28 22" fill="none" stroke="#fff" stroke-width="2.2"><path d="M2 2l9 9-9 9M9 2l9 9-9 9M16 2l9 9-9 9"/></svg>
    </div>
    <div class="foot">PROJECT OVERSIGHT</div>
  </section>

  <!-- row 1 -->
  <section class="slide c1 r1">
    <div class="photo blue" style="inset:0" role="img" aria-label="Blue-toned photo of an engineer's desk with drawing tools"></div>
    <div class="hero-text" style="position:absolute;left:20px;top:64px;width:70px">
      <div class="kicker">Write a great text here</div>
      <div class="big">About</div>
      <div class="big heavy">VELTIQ</div>
      <div class="fine">Keep working toward the goal each day and results will follow.</div>
    </div>
  </section>

  <section class="slide c2 r1">
    <div class="brand">VELTIQ<span class="num">3</span></div>
    <div class="photo" style="left:16px;top:32px;width:92px;height:62px" role="img" aria-label="Photo of the founder reading a newspaper"></div>
    <div style="position:absolute;left:115px;top:40px;width:70px;border-left:1px solid var(--navy);padding-left:3px">
      <div class="kicker">Write a great text here</div>
      <div class="title" style="font-size:8px">Message from the</div>
      <div class="title hl" style="font-size:10px;color:var(--blue)">Founder</div>
    </div>
    <div class="fine" style="position:absolute;left:118px;top:69px;width:66px">Keep working toward the goal each day and results will follow.</div>
    <div class="footer">PROJECT OVERSIGHT</div>
  </section>

  <section class="slide c3 r1">
    <div class="brand">VELTIQ<span class="num">4</span></div>
    <div class="photo dark" style="left:0;top:32px;width:88px;height:62px" role="img" aria-label="Photo of a business handshake"></div>
    <div style="position:absolute;left:88px;top:32px;width:212px;max-width:124px;height:62px;background:var(--blue);padding:9px 0 0 30px">
      <div class="hero-text" style="width:66px">
        <div class="kicker">Write a great text here</div>
        <div class="big">About</div>
        <div class="big heavy">VELTIQ</div>
        <div class="fine">Keep working toward the goal each day and results will follow.</div>
      </div>
    </div>
    <div class="footer">PROJECT OVERSIGHT</div>
  </section>

  <!-- row 2 -->
  <section class="slide c1 r2">
    <div class="brand">VELTIQ<span class="num">5</span></div>
    <div class="heading"><div class="kicker">Write a great title here</div><div class="title">Our <span class="hl">Story</span></div></div>
    <div class="fine" style="position:absolute;left:20px;top:29px;width:192px">
      <p>Our team guides complex builds from first plan to final handover. We track cost, time and risk for every client and report clearly at each stage, so leaders can act with confidence and keep each project on course toward its goals.</p>
      <p>Our team guides complex builds from first plan to final handover. We track cost, time and risk for every client and report clearly at each stage, so leaders can act with confidence and keep each project on course toward its goals.</p>
      <p>Our team guides complex builds from first plan to final handover. We track cost, time and risk for every client and report clearly at each stage, so leaders can act with confidence and keep each project on course toward its goals.</p>
    </div>
    <div class="footer">PROJECT OVERSIGHT</div>
  </section>

  <section class="slide c2 r2">
    <div class="brand">VELTIQ<span class="num">6</span></div>
    <div class="heading"><div class="kicker">Write a great title here</div><div class="title">Our <span class="hl">Beginning</span></div></div>
    <div class="fine" style="position:absolute;left:20px;top:27px;width:92px">
      <p>Our team guides complex builds from first plan to final handover. We track cost, time and risk for every client and report clearly at each stage, so leaders can act with confidence and keep each project on course toward its goals.</p>
      <p>Our team guides complex builds from first plan to final handover. We track cost, time and risk for every client and report clearly at each stage, so leaders can act with confidence and keep each project on course toward its goals.</p>
    </div>
    <div class="fine" style="position:absolute;left:118px;top:27px;width:92px">
      <p>Our team guides complex builds from first plan to final handover. We track cost, time and risk for every client and report clearly at each stage, so leaders can act with confidence and keep each project on course toward its goals.</p>
      <p>Our team guides complex builds from first plan to final handover. We track cost, time and risk for every client and report clearly at each stage, so leaders can act with confidence and keep each project on course toward its goals.</p>
    </div>
    <div class="footer">PROJECT OVERSIGHT</div>
  </section>

  <section class="slide c3 r2">
    <div class="brand">VELTIQ<span class="num">7</span></div>
    <div class="heading"><div class="kicker">Write a great title here</div><div class="title">Our Company <span class="hl">Through the Time</span></div></div>
    <div class="milestone" style="left:21px">
      <div class="icon"><svg width="9" height="8" viewBox="0 0 9 8"><path d="M4.5 0L0 4h1.3v4h2.4V5.5h1.6V8h2.4V4H9z" fill="var(--blue)"/></svg></div>
      <div class="year">1990</div><div class="label">Our Beginning</div><div class="fine">Short note on this milestone.</div>
    </div>
    <div class="arrow-dot" style="left:79px"><svg width="6" height="5" viewBox="0 0 6 5" fill="none" stroke="#fff" stroke-width=".8"><path d="M.5.5l2 2-2 2M3 .5l2 2-2 2"/></svg></div>
    <div class="milestone" style="left:85px;margin-left:0">
      <div class="icon"><svg width="8" height="9" viewBox="0 0 8 9"><path d="M1 0v9" stroke="var(--navy)" stroke-width=".8"/><path d="M1.4.6h5.8L5.5 2.5l1.7 2H1.4z" fill="var(--navy)"/></svg></div>
      <div class="year">2000</div><div class="label">Our First Building</div><div class="fine">Short note on this milestone.</div>
    </div>
    <div class="arrow-dot" style="left:144px"><svg width="6" height="5" viewBox="0 0 6 5" fill="none" stroke="#fff" stroke-width=".8"><path d="M.5.5l2 2-2 2M3 .5l2 2-2 2"/></svg></div>
    <div class="milestone" style="left:150px">
      <div class="icon"><svg width="9" height="9" viewBox="0 0 9 9"><path d="M2 0h5v3a2.5 2.5 0 01-5 0zM4 5.5h1V7h1.5v1.5h-4V7H4z" fill="var(--blue)"/><path d="M2 1H.5v1A1.5 1.5 0 002 3.5M7 1h1.5v1A1.5 1.5 0 017 3.5" fill="none" stroke="var(--blue)" stroke-width=".5"/></svg></div>
      <div class="year">2010</div><div class="label">Our First Franchise</div><div class="fine">Short note on this milestone.</div>
    </div>
    <div class="footer">PROJECT OVERSIGHT</div>
  </section>

  <!-- row 3 -->
  <section class="slide c1 r3">
    <div class="photo" style="inset:0" role="img" aria-label="Photo of a smiling business team in an office"></div>
    <div class="slide-wordmark">VELTIQ</div>
    <div class="band"><div class="heading-w"><div class="kicker">Write a great title here</div><div class="title">Meet our Team</div></div></div>
  </section>

  <section class="slide c2 r3">
    <div class="brand">VELTIQ<span class="num">9</span></div>
    <div class="heading"><div class="kicker">Write a great title here</div><div class="title">Meet our Awesome <span class="hl">Team</span></div></div>
    <div class="member" style="left:20px"><div class="photo" role="img" aria-label="Portrait photo of a team member"></div><div class="label">John Doe</div><div class="fine">A few words about this person.</div><div class="socials"><i></i><i></i><i></i><i></i></div></div>
    <div class="member" style="left:62px"><div class="photo dark" role="img" aria-label="Portrait photo of a team member"></div><div class="label">Jane Doe</div><div class="fine">A few words about this person.</div><div class="socials"><i></i><i></i><i></i><i></i></div></div>
    <div class="member" style="left:104px"><div class="photo" role="img" aria-label="Portrait photo of a team member"></div><div class="label">John Doe</div><div class="fine">A few words about this person.</div><div class="socials"><i></i><i></i><i></i><i></i></div></div>
    <div class="member" style="left:146px"><div class="photo cool" role="img" aria-label="Portrait photo of a team member"></div><div class="label">Jane Doe</div><div class="fine">A few words about this person.</div><div class="socials"><i></i><i></i><i></i><i></i></div></div>
    <div class="footer">PROJECT OVERSIGHT</div>
  </section>

  <section class="slide c3 r3">
    <div class="brand">VELTIQ<span class="num">10</span></div>
    <div class="heading"><div class="kicker">Write a great title here</div><div class="title">Our <span class="hl">Projects</span></div></div>
    <div style="position:absolute;left:0;top:27px;width:93px;height:39px;background:var(--blue-deep);color:#fff;font-size:4px;font-weight:700;text-align:center;line-height:1.2;padding:7px 10px">Lorem ipsum dolor sit amet, consectetur adipiscing elit. Praesent molestie efficitur est,</div>
    <div class="photo" style="left:94px;top:27px;width:43px;height:39px" role="img" aria-label="Photo of colleagues reviewing documents"></div>
    <div class="photo site" style="left:138px;top:27px;width:43px;height:39px" role="img" aria-label="Photo of a construction site with cranes"></div>
    <div class="photo" style="left:182px;top:27px;width:44px;height:39px" role="img" aria-label="Photo of hands working on a report"></div>
    <div style="position:absolute;left:0;top:68px;width:49px;height:39px;background:#333"></div>
    <div class="photo cool" style="left:50px;top:68px;width:43px;height:39px" role="img" aria-label="Photo of people standing in a bright office"></div>
    <div class="photo" style="left:94px;top:68px;width:43px;height:39px" role="img" aria-label="Photo of a person using a tablet"></div>
    <div style="position:absolute;left:138px;top:68px;width:43px;height:39px;background:var(--blue);color:#fff;padding:3px 4px">
      <div style="font-size:7px;font-weight:900;line-height:.8">&ldquo;</div>
      <div class="fine" style="color:#e6eef7;font-size:2.3px">A short quote from a client.</div>
    </div>
    <div class="photo" style="left:182px;top:68px;width:44px;height:39px" role="img" aria-label="Photo of a person writing at a desk"></div>
    <div class="footer">PROJECT OVERSIGHT</div>
  </section>

  <!-- row 4 -->
  <section class="slide c1 r4">
    <div class="photo cool" style="inset:0" role="img" aria-label="Blurred photo of business people walking in an office"></div>
    <div class="slide-wordmark">VELTIQ</div>
    <div class="band"><div class="heading-w"><div class="kicker">Write a great title here</div><div class="title">Our Services</div></div></div>
  </section>

  <section class="slide c2 r4">
    <div class="brand">VELTIQ<span class="num">12</span></div>
    <div class="heading"><div class="kicker">Write a great title here</div><div class="title">Our Latest <span class="hl">Projects</span></div></div>
    <div class="photo site" style="left:17px;top:30px;width:62px;height:62px" role="img" aria-label="Photo of construction workers on site"><div class="caption"><b>Project Name</b><span>Brief line about the project.</span></div></div>
    <div class="photo" style="left:84px;top:30px;width:62px;height:62px" role="img" aria-label="Photo of a hand pointing at a chart on screen"><div class="caption"><b>Project Name</b><span>Brief line about the project.</span></div></div>
    <div class="photo" style="left:150px;top:30px;width:62px;height:62px" role="img" aria-label="Photo of a person using a tablet"><div class="caption"><b>Project Name</b><span>Brief line about the project.</span></div></div>
    <div class="footer">PROJECT OVERSIGHT</div>
  </section>

  <section class="slide c3 r4">
    <div class="brand">VELTIQ<span class="num">13</span></div>
    <div class="heading"><div class="kicker">Write a great title here</div><div class="title">Our Latest <span class="hl">Projects</span></div></div>
    <div style="position:absolute;left:33px;top:27px;width:90px">
      <div class="label">Project Name</div>
      <div class="fine" style="font-size:2.2px">Our team guides complex builds from first plan to final handover. We track cost, time and risk for every client and report clearly at each stage, so leaders can act with confidence and keep each project on course toward its goals.</div>
      <div class="label" style="margin-top:3px">Description of our projects</div>
      <div class="fine" style="font-size:2.2px">Our team guides complex builds from first plan to final handover. We track cost, time and risk for every client and report clearly at each stage, so leaders can act with confidence and keep each project on course toward its goals.</div>
    </div>
    <div class="photo" style="left:150px;top:30px;width:62px;height:62px" role="img" aria-label="Photo of a person using a tablet"><div class="caption"><b>Project Name</b><span>Brief line about the project.</span></div></div>
    <div class="footer">PROJECT OVERSIGHT</div>
  </section>

  <!-- row 5 -->
  <section class="slide c1 r5">
    <div class="brand">VELTIQ<span class="num">14</span></div>
    <div class="heading"><div class="kicker">Write a great title here</div><div class="title">Our Latest <span class="hl">Projects</span></div></div>
    <div class="photo" style="left:17px;top:30px;width:62px;height:62px" role="img" aria-label="Photo of hands reviewing printed charts"><div class="caption"><b>PROJECT NAME</b><span>Brief line about the project.</span></div></div>
    <div style="position:absolute;left:105px;top:27px;width:92px">
      <div class="label">Project Name</div>
      <div class="fine" style="font-size:2.2px">Our team guides complex builds from first plan to final handover. We track cost, time and risk for every client and report clearly at each stage, so leaders can act with confidence and keep each project on course toward its goals.</div>
      <div class="label" style="margin-top:3px">Description of our projects</div>
      <div class="fine" style="font-size:2.2px">Our team guides complex builds from first plan to final handover. We track cost, time and risk for every client and report clearly at each stage, so leaders can act with confidence and keep each project on course toward its goals.</div>
    </div>
    <div class="footer">PROJECT OVERSIGHT</div>
  </section>

  <section class="slide c2 r5">
    <div class="brand">VELTIQ<span class="num">15</span></div>
    <div class="heading"><div class="kicker">Write a great title here</div><div class="title">Our Latest <span class="hl">Projects</span></div></div>
    <div class="photo site" style="left:15px;top:29px;width:48px;height:63px" role="img" aria-label="Photo of a construction site"><div class="caption"><b>Project Name</b><span>Brief line about the project.</span></div></div>
    <div class="photo cool" style="left:65px;top:29px;width:48px;height:63px" role="img" aria-label="Photo of business people in an office"><div class="caption"><b>Project Name</b><span>Brief line about the project.</span></div></div>
    <div class="photo" style="left:115px;top:29px;width:48px;height:63px" role="img" aria-label="Photo of a hand pointing at a monitor"><div class="caption"><b>Project Name</b><span>Brief line about the project.</span></div></div>
    <div class="photo" style="left:165px;top:29px;width:48px;height:63px" role="img" aria-label="Photo of hands reviewing printed charts"><div class="caption"><b>Project Name</b><span>Brief line about the project.</span></div></div>
    <div class="footer">PROJECT OVERSIGHT</div>
  </section>

  <section class="slide c3 r5">
    <div class="photo blue" style="inset:0" role="img" aria-label="Blue-toned photo of a handshake over a tablet showing charts"></div>
    <div class="slide-wordmark light">VELTIQ</div>
    <div class="band"><div class="heading-w"><div class="kicker">Write a great title here</div><div class="title">Stats &amp; Reports</div></div></div>
  </section>

  <!-- row 6 -->
  <section class="slide c1 r6">
    <div class="brand">VELTIQ<span class="num">17</span></div>
    <div class="heading"><div class="kicker">Write a great title here</div><div class="title">Analytics <span class="hl">Three Facts</span></div></div>
    <div style="position:absolute;left:18px;top:32px;width:88px">
      <div class="label" style="text-transform:none">Analysis of the Chart</div>
      <div class="fine">Our team guides complex builds from first plan to final handover. We track cost, time and risk for every client and report clearly at each stage, so leaders can act with confidence and keep each project on course toward its goals.</div>
      <div style="display:flex;gap:2px;margin-top:4px">
        <span style="width:7px;height:7px;border-radius:50%;background:var(--navy)"></span>
        <span style="width:7px;height:7px;border-radius:50%;background:var(--navy)"></span>
        <span style="width:7px;height:7px;border-radius:50%;background:var(--navy)"></span>
      </div>
    </div>
    <svg class="chart" style="left:116px;top:36px" width="100" height="68" viewBox="0 0 100 68">
      <g stroke="#e3e6ea" stroke-width=".3"><path d="M8 8h90M8 20h90M8 32h90M8 44h90"/></g>
      <path d="M8 56V60h90" stroke="#999" stroke-width=".3" fill="none"/>
      <path d="M8 22L38 44L68 38L98 12V58H8z" fill="var(--blue)"/>
      <path d="M8 46L30 28L52 42L75 46L98 44V58H8z" fill="var(--navy)"/>
      <g font-size="2" fill="#888" font-family="Lato,sans-serif"><text x="10" y="63">Category 1</text><text x="36" y="63">Category 2</text><text x="62" y="63">Category 3</text><text x="86" y="63">Category 4</text></g>
    </svg>
    <div class="footer">PROJECT OVERSIGHT</div>
  </section>

  <section class="slide c2 r6">
    <div class="brand">VELTIQ<span class="num">18</span></div>
    <div class="heading"><div class="kicker">Write a great title here</div><div class="title">Comparison <span class="hl">Bar Graphics</span></div></div>
    <div style="position:absolute;left:20px;top:36px;width:75px;display:flex;flex-direction:column;gap:6px">
      <div style="display:flex;gap:3px"><span style="flex:none;width:10px;height:10px;border-radius:50%;background:var(--blue)"></span><div><div class="label" style="text-transform:none;font-size:2.6px">Factor Number One</div><div class="fine" style="font-size:2.1px">Short note on this factor.</div></div></div>
      <div style="display:flex;gap:3px"><span style="flex:none;width:10px;height:10px;border-radius:50%;background:var(--navy)"></span><div><div class="label" style="text-transform:none;font-size:2.6px">Factor Number Two</div><div class="fine" style="font-size:2.1px">Short note on this factor.</div></div></div>
      <div style="display:flex;gap:3px"><span style="flex:none;width:10px;height:10px;border-radius:50%;background:var(--blue)"></span><div><div class="label" style="text-transform:none;font-size:2.6px">Factor Number Three</div><div class="fine" style="font-size:2.1px">Short note on this factor.</div></div></div>
    </div>
    <svg class="chart" style="left:100px;top:34px" width="118" height="66" viewBox="0 0 118 66">
      <path d="M6 2v56h50M64 2v56h50" stroke="#bbb" stroke-width=".3" fill="none"/>
      <g fill="var(--navy)"><rect x="10" y="26" width="2" height="32"/><rect x="22" y="30" width="2" height="28"/><rect x="34" y="34" width="2" height="24"/><rect x="46" y="18" width="2" height="40"/>
        <rect x="68" y="30" width="2" height="28"/><rect x="80" y="26" width="2" height="32"/><rect x="92" y="38" width="2" height="20"/><rect x="104" y="22" width="2" height="36"/></g>
      <g fill="var(--blue)"><rect x="13" y="40" width="2" height="18"/><rect x="25" y="20" width="2" height="38"/><rect x="37" y="24" width="2" height="34"/><rect x="49" y="14" width="2" height="44"/>
        <rect x="71" y="22" width="2" height="36"/><rect x="83" y="36" width="2" height="22"/><rect x="95" y="30" width="2" height="28"/><rect x="107" y="16" width="2" height="42"/></g>
      <g font-size="1.8" fill="#888" font-family="Lato,sans-serif"><text x="8" y="62">Category 1 · 2 · 3 · 4</text><text x="66" y="62">Category 1 · 2 · 3 · 4</text></g>
    </svg>
    <div class="footer">PROJECT OVERSIGHT</div>
  </section>

  <section class="slide c3 r6">
    <div class="brand"><span class="num">19</span></div>
    <div class="heading"><div class="kicker">Write a great title here</div><div class="title">Comparison <span class="hl">Chart</span></div></div>
    <svg class="chart" style="left:18px;top:34px" width="96" height="60" viewBox="0 0 96 60">
      <g stroke="#eee" stroke-width=".3"><path d="M6 10h88M6 22h88M6 34h88M6 46h88"/></g>
      <path d="M6 4v52h88" stroke="#bbb" stroke-width=".3" fill="none"/>
      <path d="M24 18L40 38L58 22L76 34" stroke="#ccc" stroke-width=".5" fill="none"/>
      <path d="M24 40L44 24L62 34L84 16" stroke="#ccc" stroke-width=".5" fill="none"/>
      <path d="M30 30L50 44L70 28" stroke="#ddd" stroke-width=".5" fill="none"/>
    </svg>
    <svg class="chart" style="left:120px;top:34px" width="96" height="60" viewBox="0 0 96 60">
      <path d="M8 4v52h86" stroke="#bbb" stroke-width=".3" fill="none"/>
      <rect x="10" y="6" width="82" height="50" fill="var(--blue-deep)"/>
      <path d="M10 26L38 34L64 24L92 30V56H10z" fill="var(--blue)"/>
      <path d="M10 40L38 46L64 40L92 48V56H10z" fill="var(--navy)"/>
      <g font-size="1.8" fill="#888" font-family="Lato,sans-serif"><text x="0" y="8">100%</text><text x="2" y="32">50%</text><text x="4" y="56">0%</text></g>
    </svg>
    <div class="fine" style="position:absolute;left:20px;top:98px;width:190px;font-size:2.1px">Notes on the chart findings appear here in one line.</div>
    <div class="footer">PROJECT OVERSIGHT</div>
  </section>

</body>
</html>
```